Bright Path Flyer Design for Virtual Online Clinic. -5.5 x 8.5 inches (half sheet)

We need a clean, modern flyer design for Bright Path, a new virtual walk-in clinic based in British Columbia. The flyer will be used in libraries, pharmacies, and community centers to help residents easily access primary care through their Bright Path NFC access card.
The flyer will ask a question : NEED A DOCTOR? This should be large and attention grabbing.
The design should clearly feature a Bright Path card image (the access card) as the centerpiece and visually show how patients can use it to book appointments. The tone should feel trustworthy, healthcare-oriented, and community-friendly — clean fonts, clear spacing, and strong readability from a distance.

Side One: This card has the NFC Access Card.
NEED A DOCTOR? (Large Font, Attention Grabbing)
How to Book an Appointment using your Bright Path Card
Step 1: Tap Your Card on Your Phone
Hold your card near the back of your phone.
It will activate automatically — no app needed.
The Bright Path scheduler will open.
Step 2: Schedule Your Appointment
Select your clinical concern.
Choose your time window.
Register (only once).
Confirm your appointment.
Step 3: Relax, we’ll take care of the rest
A doctor will call during your scheduled time.
Once booked, you’ll be able to call our office.
No emails, no texts — just a real person.
It’s that simple.
Side Two:
About Bright Path
Created by Dr. Marcus Ferrigan
Bright Path was founded to make healthcare simple and convenient. Prescription renewals. Common infections. Medical notes. And so much more.
Our doctors can address 120+ health concerns virtually — providing quality care without the waiting room. No waiting rooms. Just real doctors providing real care.
Why Patients Choose Bright Path
Easy access – book and be seen from anywhere in BC.
Effortless booking – tap your Bright Path Card to begin.
Trusted physicians – every visit is with a licensed BC family doctor.
How It Works
Book your visit — choose a time window that fits your day.
Join the queue — you’ll be called when it’s your turn.
Speak directly with your doctor — simple, secure, and stress-free.
Convenient Care for Common Concerns

Additional Details.
Please find the domain to be launched soon. I've attached the NFC card file for review, it is 85.5 mm x 54 mm. The card will be glued to the flyer.
I've attached examples of flyers but they are not the look I am seeking and I am looking for creative solutions.
Thank you!
http://brightpath-example.test/

Adult Patients in British Columbia

Healthcare

• Looking for clean lines, uniform appearance, and high legibility i.e poppins

0054AA
0677BA
7BADD7
CADEEF
E8F1F8

• Need A Doctor?
• Elegant style, not too busy, clear layout.
• Clutter, look cheap - review examples.

```html
<!DOCTYPE html>
<html lang="en">
<head>
<meta charset="utf-8">
<title>Bright Path Flyer</title>
<link href="https://fonts.googleapis.com/css2?family=Rubik:wght@300;400;500;600&family=Roboto+Condensed:wght@800&family=Allura&display=swap" rel="stylesheet">
<style>
  :root {
    --navy: #283f8a;
    --navy-deep: #223780;
    --ink: #1f3a8f;
    --text: #1d1d2b;
    --periwinkle: #9db0ea;
    --periwinkle-soft: #c5d1f5;
    --cyan-soft: #d8f8fb;
    --paper: #ffffff;
    --backdrop: #878787;
    --nfc-fill: #f4f4f4;
    --nfc-line: #9aa3c9;
    --nfc-text: #a4a8b8;
  }
  * { box-sizing: border-box; margin: 0; padding: 0; }
  html, body { width: 949px; height: 1200px; overflow: hidden; }
  body { background: var(--backdrop); font-family: "Rubik", sans-serif; position: relative; }

  .flyer-side {
    position: absolute; left: 116px; width: 723px; height: 469px;
    background: var(--paper); overflow: hidden;
    box-shadow: 0 10px 22px rgba(0,0,0,.28);
  }
  .side-front { top: 108px; }
  .side-back { top: 643px; height: 468px; border-bottom: 4px solid var(--navy-deep); }
  .side-bg { position: absolute; inset: 0; width: 100%; height: 100%; }

  /* Front */
  .headline {
    position: absolute; left: 31px; top: 20px;
    font-family: "Roboto Condensed", sans-serif; font-weight: 800;
    font-size: 104px; line-height: 83px; letter-spacing: -1px;
    background: linear-gradient(180deg, #ffffff 0%, #e9e9e9 40%, #b9b9b9 55%, #f2f2f2 80%, #cfcfcf 100%);
    -webkit-background-clip: text; background-clip: text; color: transparent;
    filter: drop-shadow(2px 3px 2px rgba(10,20,60,.45));
  }
  .desk-doctor-art {
    position: absolute; left: 470px; top: 22px; width: 250px; height: 225px;
    border-radius: 40px 20px 0 60px;
    background: linear-gradient(160deg, #3b57c4 0%, #6f86e0 45%, #c5d1f5 100%);
    opacity: .85;
  }
  .booking-title {
    position: absolute; left: 33px; top: 237px;
    color: var(--ink); font-size: 22px; line-height: 27px; font-weight: 400;
  }
  .booking-title strong { font-weight: 600; }
  .step { position: absolute; top: 326px; width: 120px; text-align: center; }
  .step-icon {
    width: 56px; height: 56px; margin: 0 auto; border: 2.5px solid var(--ink);
    border-radius: 50%; display: flex; align-items: center; justify-content: center;
  }
  .step-label {
    margin-top: 15px; color: var(--ink); font-weight: 500; font-size: 14.5px; line-height: 16px;
  }
  .step-tap { left: 16px; }
  .step-schedule { left: 139px; }
  .step-relax { left: 270px; }
  .step-divider { position: absolute; top: 330px; width: 1px; height: 94px; background: #c9cbd6; }
  .nfc-slot {
    position: absolute; left: 400px; top: 259px; width: 291px; height: 185px;
    background: var(--nfc-fill); border: 1.5px dashed var(--nfc-line); border-radius: 14px;
    display: flex; align-items: center; justify-content: center;
    color: var(--nfc-text); font-size: 14.5px; font-weight: 300;
  }

  /* Back */
  .about-block { position: absolute; left: 20px; top: 32px; width: 270px; text-align: center; color: var(--paper); }
  .about-kicker { font-size: 17px; font-weight: 300; }
  .brand-name { margin-top: 10px; font-size: 38px; font-weight: 400; line-height: 44px; }
  .about-credit { margin-top: 16px; font-size: 16.5px; font-weight: 300; text-align: left; padding-left: 11px; white-space: nowrap; }
  .about-credit strong { font-weight: 500; }
  .about-divider { position: absolute; left: 310px; top: 35px; width: 1px; height: 106px; background: rgba(255,255,255,.8); }
  .about-copy { position: absolute; left: 333px; top: 30px; width: 372px; color: var(--paper); font-size: 14.5px; line-height: 17px; font-weight: 300; }
  .about-copy p + p { margin-top: 10px; }

  .section-title { position: absolute; color: var(--ink); font-size: 25.5px; line-height: 31px; }
  .section-title .light { font-weight: 400; display: block; }
  .section-title .bold { font-weight: 600; display: block; }
  .why-title { left: 32px; top: 194px; }
  .how-title { left: 444px; top: 222px; font-weight: 600; }

  .benefit-list { position: absolute; list-style: none; top: 270px; }
  .why-list { left: 38px; width: 240px; }
  .how-list { left: 438px; width: 260px; }
  .benefit-list li { display: flex; gap: 10px; font-size: 15px; line-height: 18.5px; color: var(--text); margin-bottom: 10.5px; }
  .benefit-list .tick { flex: none; width: 15px; height: 15px; margin-top: 2px; }
  .benefit-list b { color: var(--ink); font-weight: 500; }

  .standing-doctor-art {
    position: absolute; left: 300px; top: 185px; width: 130px; height: 230px;
    border-radius: 60px 60px 10px 10px;
    background: linear-gradient(180deg, #8fd9ec 0%, #eef3ff 45%, #1f2f6b 100%);
    opacity: .8;
  }
  .stage-line { position: absolute; left: 292px; top: 416px; width: 146px; height: 1px; background: var(--navy-deep); }
  .tagline {
    position: absolute; left: 0; right: 0; top: 420px; text-align: center;
    font-family: "Allura", cursive; font-size: 34px; color: var(--ink);
  }
</style>
</head>
<body>

<section class="flyer-side side-front">
  <svg class="side-bg" viewBox="0 0 723 469" preserveAspectRatio="none" aria-hidden="true">
    <path d="M0 243 C40 228 80 212 134 212 C240 210 330 250 430 253 C560 256 650 232 723 188 V0 H0 Z" fill="var(--periwinkle)"/>
    <path d="M0 233 C30 225 70 210 134 208 C240 205 330 244 430 247 C560 250 650 225 723 181 V0 H0 Z" fill="var(--navy)"/>
  </svg>
  <h1 class="headline">NEED A<br>DOCTOR?</h1>
  <div class="desk-doctor-art" role="img" aria-label="Illustration of a smiling doctor working on a laptop at a desk"></div>

  <h2 class="booking-title">How to Book an Appointment<br>using your <strong>BRIGHT PATH CARD</strong></h2>

  <div class="step step-tap">
    <div class="step-icon">
      <svg width="30" height="30" viewBox="0 0 30 30" fill="none" stroke="var(--ink)" stroke-width="1.6">
        <rect x="5" y="2" width="14" height="25" rx="2"/>
        <rect x="11" y="10" width="16" height="10" rx="1.5" fill="#fff"/>
        <line x1="13" y1="17" x2="24" y2="17" stroke-dasharray="1 1.2"/>
        <line x1="10" y1="24" x2="14" y2="24"/>
      </svg>
    </div>
    <p class="step-label">Tap Your Card<br>on Your Phone</p>
  </div>
  <div class="step-divider" style="left:138px"></div>
  <div class="step step-schedule">
    <div class="step-icon">
      <svg width="30" height="30" viewBox="0 0 30 30" fill="none" stroke="var(--ink)" stroke-width="1.6">
        <rect x="3" y="5" width="20" height="19" rx="2"/>
        <line x1="3" y1="10" x2="23" y2="10"/>
        <line x1="8" y1="3" x2="8" y2="7"/><line x1="18" y1="3" x2="18" y2="7"/>
        <path d="M7 14h2M12 14h2M17 14h2M7 18h2M12 18h2" />
        <circle cx="22" cy="22" r="5" fill="#fff"/>
        <path d="M19.5 22l2 2 3-3.5"/>
      </svg>
    </div>
    <p class="step-label">Schedule Your<br>Appointment</p>
  </div>
  <div class="step-divider" style="left:263px"></div>
  <div class="step step-relax">
    <div class="step-icon">
      <svg width="30" height="30" viewBox="0 0 30 30" fill="none" stroke="var(--ink)" stroke-width="1.6" stroke-linejoin="round">
        <path d="M15 15 C10 11 8 9 8 6.5 A3 3 0 0 1 15 5 A3 3 0 0 1 22 6.5 C22 9 20 11 15 15 Z"/>
        <path d="M4 14v7l5 5h4v-4l-4-4"/>
        <path d="M26 14v7l-5 5h-4v-4l4-4"/>
      </svg>
    </div>
    <p class="step-label">Relax, we’ll take<br>care of the rest</p>
  </div>

  <div class="nfc-slot">NFC Access Card.</div>
</section>

<section class="flyer-side side-back">
  <svg class="side-bg" viewBox="0 0 723 468" preserveAspectRatio="none" aria-hidden="true">
    <path d="M360 190 Q400 350 452 468 H723 V120 Z" fill="var(--cyan-soft)"/>
    <path d="M0 199 C30 188 70 170 134 170 C240 170 300 211 420 212 C560 213 660 193 723 142 V0 H0 Z" fill="var(--periwinkle)"/>
    <path d="M0 191 C30 180 70 163 134 163 C240 163 300 203 420 204 C560 205 660 185 723 135 V0 H0 Z" fill="var(--navy)"/>
  </svg>

  <div class="about-block">
    <p class="about-kicker">About</p>
    <p class="brand-name">Bright Path</p>
    <p class="about-credit">Created by <strong>Dr. Marcus Ferrigan</strong></p>
  </div>
  <div class="about-divider"></div>
  <div class="about-copy">
    <p>Bright Path was founded to make healthcare simple and convenient. Prescription renewals. Common infections. Medical notes. And so much more.</p>
    <p>Our doctors can address 120+ health concerns virtually — providing quality care without the waiting room. No waiting rooms. Just real doctors providing real care.</p>
  </div>

  <h2 class="section-title why-title"><span class="light">Why Patients</span><span class="bold">Choose Bright Path</span></h2>
  <ul class="benefit-list why-list">
    <li><svg class="tick" viewBox="0 0 16 16"><circle cx="8" cy="8" r="8" fill="var(--ink)"/><path d="M4.5 8.2l2.4 2.3 4.6-4.8" stroke="#fff" stroke-width="1.8" fill="none"/></svg><span><b>Easy access –</b> book and be seen from anywhere in BC.</span></li>
    <li><svg class="tick" viewBox="0 0 16 16"><circle cx="8" cy="8" r="8" fill="var(--ink)"/><path d="M4.5 8.2l2.4 2.3 4.6-4.8" stroke="#fff" stroke-width="1.8" fill="none"/></svg><span><b>Effortless booking –</b> tap your Bright Path Card to begin.</span></li>
    <li><svg class="tick" viewBox="0 0 16 16"><circle cx="8" cy="8" r="8" fill="var(--ink)"/><path d="M4.5 8.2l2.4 2.3 4.6-4.8" stroke="#fff" stroke-width="1.8" fill="none"/></svg><span><b>Trusted physicians –</b> every visit is with a licensed BC family doctor.</span></li>
  </ul>

  <div class="standing-doctor-art" role="img" aria-label="Illustration of a standing doctor in a white coat with speech bubbles"></div>
  <div class="stage-line"></div>

  <h2 class="section-title how-title">How It Works</h2>
  <ul class="benefit-list how-list">
    <li><svg class="tick" viewBox="0 0 16 16"><circle cx="8" cy="8" r="8" fill="var(--ink)"/><path d="M4.5 8.2l2.4 2.3 4.6-4.8" stroke="#fff" stroke-width="1.8" fill="none"/></svg><span><b>Book your visit –</b> choose a time window that fits your day.</span></li>
    <li><svg class="tick" viewBox="0 0 16 16"><circle cx="8" cy="8" r="8" fill="var(--ink)"/><path d="M4.5 8.2l2.4 2.3 4.6-4.8" stroke="#fff" stroke-width="1.8" fill="none"/></svg><span><b>Join the queue–</b> you’ll be called when it’s your turn.</span></li>
    <li><svg class="tick" viewBox="0 0 16 16"><circle cx="8" cy="8" r="8" fill="var(--ink)"/><path d="M4.5 8.2l2.4 2.3 4.6-4.8" stroke="#fff" stroke-width="1.8" fill="none"/></svg><span><b>Speak directly with your doctor –</b> simple, secure, and stress-free.</span></li>
  </ul>

  <p class="tagline">Convenient Care for Common Concerns</p>
</section>

</body>
</html>
```